Aerial Photography Brochure

I need a brochure designed around my company logo and around aerial photography. We use drones to capture jobsite progression, real estate, and commercial jobs. I like designs with the color blue and that show people we are professional and sophisticated.

Industry/Entity Type

Real Estate

Font styles to use
Serif

Colors
3276b5
0293ce
33a6d7
86cae7
85abd2
3176b5
0355a3

Requirements
Must have
• Must have My logo and our info to contact and to view our website.
Nice to have
• Not crazy artistic i just want something that looks very professional and gets people to look at my website
Should not have
• Hours of operation

```html
<!DOCTYPE html>
<html lang="en">
<head>
<meta charset="utf-8">
<title>Skyline Vantage Imaging – Brochure</title>
<link rel="stylesheet" href="https://fonts.googleapis.com/css2?family=Cinzel:wght@400;700&family=Lato:wght@400;700&display=swap">
<style>
  :root{
    --blue-deep:#0355a3;
    --blue-main:#3276b5;
    --blue-alt:#3176b5;
    --blue-bright:#0293ce;
    --blue-mid:#33a6d7;
    --blue-soft:#86cae7;
    --blue-muted:#85abd2;
    --sky-deep:#1668c4;
    --sky-glow:#e8f4fb;
    --haze:#dce8f2;
    --city-steel:#5f81a5;
    --city-night:#1e3f6b;
    --paper:#ffffff;
    --paper-shade:#eceff3;
    --rule-grey:#9aa3ad;
    --ink:#1f2a36;
    --ink-logo:#2a64a6;
    --backdrop:#d9dbde;
  }
  *{box-sizing:border-box;margin:0;padding:0}
  html,body{width:1200px;height:847px;overflow:hidden;background:var(--backdrop)}
  .canvas{position:relative;width:1200px;height:847px;display:flex;gap:20px;justify-content:center;align-items:center}
  .page{position:relative;width:560px;height:797px;background:linear-gradient(180deg,var(--paper) 45%,var(--paper-shade));overflow:hidden;box-shadow:0 6px 18px rgba(0,0,0,.25)}
  .photo{position:absolute;left:0;top:0;width:100%}
  .photo--house{
    height:470px;
    background:
      radial-gradient(ellipse 70% 55% at 42% 68%, var(--sky-glow) 0%, rgba(232,244,251,.85) 35%, rgba(232,244,251,0) 70%),
      radial-gradient(ellipse 45% 30% at 85% 20%, rgba(134,202,231,.55), rgba(134,202,231,0) 70%),
      linear-gradient(180deg,var(--sky-deep) 0%,var(--blue-bright) 40%,var(--blue-soft) 100%);
  }
  .photo--city{
    height:440px;
    background:
      radial-gradient(ellipse 60% 35% at 65% 18%, rgba(255,255,255,.9), rgba(255,255,255,0) 70%),
      linear-gradient(180deg,var(--haze) 0%,var(--blue-muted) 30%,var(--city-steel) 58%,var(--city-night) 100%);
  }
  .shape{position:absolute;left:0;top:0;width:100%;height:100%}
  .brand{position:absolute;display:flex;align-items:center;gap:12px;font-family:"Cinzel",serif;font-weight:400;color:var(--ink-logo)}
  .brand__mark{width:22px;height:22px;border-radius:50%;background:var(--blue-bright);flex:none}
  .brand__name{line-height:1.05;text-align:left}
  .brand--cover{left:120px;top:508px}
  .brand--cover .brand__name{font-size:32px;letter-spacing:1px}
  .brand--inner{right:30px;top:40px}
  .brand--inner .brand__mark{width:18px;height:18px}
  .brand--inner .brand__name{font-size:23px;letter-spacing:1px}
  .contact{position:absolute;left:0;right:0;text-align:center;color:#fff;font-family:"Lato",sans-serif}
  .contact__phone{font-size:21px;font-weight:700;letter-spacing:.3px}
  .contact__email{font-size:13px;margin-top:5px}
  .contact__web{font-size:13px;letter-spacing:2px;margin-top:5px}
  .contact--cover{top:690px}
  .contact--inner{top:668px}
  .headline{position:absolute;left:70px;right:70px;top:452px;height:58px;background:linear-gradient(90deg,var(--blue-mid),var(--blue-soft) 55%,var(--blue-mid));display:flex;align-items:center;justify-content:center;font-family:"Cinzel",serif;font-weight:700;font-size:34px;letter-spacing:2px;color:var(--blue-deep);box-shadow:0 2px 6px rgba(3,85,163,.2)}
  .intro{position:absolute;left:48px;right:48px;top:532px;text-align:center;font-family:"Lato",sans-serif;font-size:11.5px;line-height:1.5;color:var(--ink)}
</style>
</head>
<body>
<main class="canvas">

  <section class="page page--cover">
    <div class="photo photo--house" role="img" aria-label="Photograph of a modern white villa with glass walls under a blue sky, a white camera drone hovering above"></div>
    <svg class="shape" viewBox="0 0 560 797" preserveAspectRatio="none" aria-hidden="true">
      <path d="M0 440 Q300 470 560 335 L560 362 Q300 495 0 465 Z" fill="var(--blue-bright)"/>
      <path d="M0 465 Q300 495 560 362 L560 380 Q300 512 0 480 Z" fill="var(--blue-soft)"/>
      <path d="M0 480 Q300 512 560 380 L560 797 L0 797 Z" fill="var(--paper)"/>
      <path d="M0 652 Q300 640 560 592 L560 603 Q300 652 0 664 Z" fill="var(--rule-grey)"/>
      <path d="M0 664 Q300 652 560 603 L560 797 L0 797 Z" fill="var(--blue-main)"/>
      <path d="M0 735 Q300 705 560 665 L560 797 L0 797 Z" fill="var(--blue-deep)" opacity=".35"/>
    </svg>
    <div class="brand brand--cover"><span class="brand__mark"></span><span class="brand__name">Skyline Vantage<br>Imaging</span></div>
    <div class="contact contact--cover">
      <p class="contact__phone">CALL US: 123 456 7890</p>
      <p class="contact__email">LOREM@lorem ipsum</p>
      <p class="contact__web">www.skylinevantageimaging.com</p>
    </div>
  </section>

  <section class="page page--inner">
    <div class="photo photo--city" role="img" aria-label="Aerial photograph of a dense city skyline with skyscrapers under a hazy sky"></div>
    <svg class="shape" viewBox="0 0 560 797" preserveAspectRatio="none" aria-hidden="true">
      <path d="M0 300 Q260 430 560 310 L560 330 Q260 450 0 318 Z" fill="var(--blue-bright)"/>
      <path d="M0 318 Q260 450 560 330 L560 345 Q260 462 0 332 Z" fill="var(--blue-soft)"/>
      <path d="M0 332 Q260 462 560 345 L560 797 L0 797 Z" fill="var(--paper)"/>
      <path d="M0 625 Q300 620 560 590 L560 600 Q300 632 0 637 Z" fill="var(--rule-grey)"/>
      <path d="M0 637 Q300 632 560 600 L560 797 L0 797 Z" fill="var(--blue-main)"/>
      <path d="M0 720 Q300 690 560 660 L560 797 L0 797 Z" fill="var(--blue-deep)" opacity=".35"/>
    </svg>
    <div class="brand brand--inner"><span class="brand__mark"></span><span class="brand__name">Skyline Vantage<br>Imaging</span></div>
    <h1 class="headline">LOREM IPSUM</h1>
    <p class="intro">Lorem Ipsum is simply dummy text of the printing and typesetting industry. Lorem Ipsum has been the industry's standard dummy text ever since the 1500s, when an unknown printer took a galley of type and scrambled it to make a type specimen book.</p>
    <div class="contact contact--inner">
      <p class="contact__phone">CALL US: 123 456 7890</p>
      <p class="contact__email">LOREM@lorem ipsum</p>
      <p class="contact__web">www.skylinevantageimaging.com</p>
    </div>
  </section>

</main>
</body>
</html>
```